Visitenkarte und Briefdesign
Zielgruppe
Limousinenservice (Stretchlimousinen)
Aufgabenstellung
Ich benötige eine Visitenkarte und ein Briefdesign in einer edlen Optik.
Auf folgender Seite können Informationen oder Bilder eingeholt werden
www.karossa-fahrten.com
Ich mag einen Hintergrund in einer Lederoptik,( wie das Logo in Anhang, BILD x4)

```html
<!DOCTYPE html>
<html lang="de">
<head>
<meta charset="utf-8">
<title>Karossa VIP – Briefbogen und Visitenkarte</title>
<link href="https://fonts.googleapis.com/css2?family=Carlito:wght@400;700&display=swap" rel="stylesheet">
<style>
  :root {
    --leather: #1c1c1c;
    --leather-light: #2e2e2e;
    --paper: #f1f1f1;
    --paper-light: #fafafa;
    --ink: #111111;
    --muted: #8a8a8a;
    --silver: #d9d9d9;
    --photo-dark: #2a2a2e;
    --photo-mid: #5a5a62;
  }
  * { margin: 0; padding: 0; box-sizing: border-box; }
  html, body { width: 849px; height: 1200px; overflow: hidden; background: var(--paper); }
  body { font-family: "Carlito", "Calibri", sans-serif; color: var(--ink); }

  .letterhead {
    position: relative; width: 849px; height: 1200px;
    background: radial-gradient(ellipse at 40% 55%, var(--paper-light), #e6e6e6 80%);
    overflow: hidden;
  }
  .leather-band { position: absolute; top: 0; left: 0; }

  .brand {
    position: absolute; top: 38px; right: 38px; width: 130px; height: 82px;
    display: flex; align-items: center; justify-content: center; gap: 8px;
    color: var(--silver); font-size: 22px; font-weight: 700; letter-spacing: 1px;
  }
  .brand-dot { width: 12px; height: 12px; border-radius: 50%; background: var(--silver); }

  .company-info {
    position: absolute; top: 160px; right: 30px; text-align: right;
    color: var(--silver); text-transform: uppercase; line-height: 1.15;
  }
  .company-info .name { font-size: 15px; font-weight: 700; letter-spacing: .3px; }
  .company-info .owner { font-size: 10px; margin-bottom: 12px; }
  .company-info .line { font-size: 14px; }
  .company-info .note { font-size: 9px; margin-bottom: 12px; }
  .company-info .gap { margin-bottom: 12px; }

  .sender-line { position: absolute; top: 198px; left: 70px; font-size: 13px; color: var(--muted); }
  .recipient { position: absolute; top: 234px; left: 72px; font-size: 15.5px; line-height: 1.3; }
  .recipient .name { font-weight: 700; }

  .date { position: absolute; top: 412px; right: 66px; font-size: 13.5px; }
  .subject { position: absolute; top: 459px; left: 72px; font-size: 15px; font-weight: 700; }
  .subject span { display: inline-block; width: 72px; }
  .body-text { position: absolute; top: 520px; left: 72px; font-size: 15px; line-height: 1.3; }
  .body-text p { margin-bottom: 18px; }
  .closing { position: absolute; top: 660px; left: 72px; font-size: 15px; }
  .signature { position: absolute; top: 760px; left: 72px; font-size: 12.5px; }

  .business-card {
    position: absolute; top: 860px; width: 320px; height: 186px; overflow: hidden;
    box-shadow: 0 6px 18px rgba(0,0,0,.35);
  }
  .card-back { left: 72px; background: #ffffff; }
  .card-front { left: 430px; background: var(--leather); }
  .card-back svg, .card-front svg { position: absolute; inset: 0; }
  .card-text {
    position: absolute; top: 16px; left: 16px; text-transform: uppercase;
    font-size: 12px; line-height: 1.12; color: var(--ink);
  }
  .card-text .name { font-weight: 700; font-size: 13px; }
  .card-text .small { font-size: 8px; margin-bottom: 5px; }
  .card-back .card-brand {
    position: absolute; right: 18px; bottom: 62px; color: var(--silver);
    font-size: 17px; font-weight: 700;
  }
  .card-photo {
    position: absolute; top: 0; left: 0; width: 320px; height: 186px;
    background: linear-gradient(160deg, var(--photo-mid), var(--photo-dark) 70%);
  }
  .card-front .card-brand {
    position: absolute; right: 16px; bottom: 52px; color: var(--silver);
    font-size: 16px; font-weight: 700;
  }

  .bottom-band {
    position: absolute; left: 0; bottom: 0; width: 849px; height: 46px;
    background: linear-gradient(180deg, var(--leather-light), var(--leather));
  }
</style>
</head>
<body>
<main class="letterhead">
  <svg class="leather-band" width="849" height="360" viewBox="0 0 849 360" aria-hidden="true">
    <defs>
      <linearGradient id="leather" x1="0" y1="0" x2="1" y2="1">
        <stop offset="0" stop-color="#2e2e2e"/>
        <stop offset="1" stop-color="#161616"/>
      </linearGradient>
    </defs>
    <path d="M0,0 H849 V345 H668 Q622,345 600,306 L462,78 Q448,54 420,54 H0 Z" fill="url(#leather)"/>
    <path d="M0,54 H420 Q448,54 462,78 L520,174 Q400,205 0,212 Z" fill="#e0e0e0" opacity=".55"/>
    <line x1="650" y1="340" x2="845" y2="260" stroke="#ffffff" stroke-width="1" opacity=".5"/>
  </svg>

  <div class="brand"><span class="brand-dot"></span>KAROSSA VIP</div>

  <div class="company-info">
    <div class="name">Limousinenservice Karossa VIP</div>
    <div class="owner">Inhaber: Jonas Brenner</div>
    <div class="line">Lindenallee 42</div>
    <div class="line gap">48155 Ahlen</div>
    <div class="line">E-Mail: info@karossa-vip.de</div>
    <div class="line">Tel.: 0170-5558214</div>
    <div class="note">(24 Stunden erreichbar)</div>
    <div class="line">www.karossa-fahrten.com</div>
    <div class="line">www.karossa-vip.de</div>
  </div>

  <div class="sender-line">Karossa VIP, Lindenallee 42, 48155 Ahlen</div>
  <div class="recipient">
    <div class="name">Max Mustermann</div>
    <div>Musterstraße 1</div>
    <div>23456 Musterstadt</div>
  </div>

  <div class="date">Ahlen, den 08.07.2014</div>
  <div class="subject"><span>Betreff:</span>Musterrechnung vom 01.01.2014</div>
  <div class="body-text">
    <p>Sehr geehrte Damen und Herren,</p>
    <p>die ist ein Beispieltext</p>
  </div>
  <div class="closing">Mit freundlichen Grüßen</div>
  <div class="signature">Jonas Brenner - Karossa VIP</div>

  <section class="business-card card-back">
    <svg width="320" height="186" viewBox="0 0 320 186" aria-hidden="true">
      <path d="M0,0 H320 V186 H250 Q225,186 215,160 L170,40 Q158,10 130,10 H0 Z" fill="none"/>
      <path d="M200,0 H320 V186 H260 Q238,186 230,164 L196,70 Q188,48 200,0 Z" fill="#1c1c1c"/>
      <path d="M0,0 H200 Q188,30 196,70 L0,20 Z" fill="#1c1c1c" opacity="0"/>
    </svg>
    <div class="card-text">
      <div class="name">Limousinenservice</div>
      <div class="name">Karossa VIP</div>
      <div class="small">Inhaber: Jonas Brenner</div>
      <div>Lindenallee 42</div>
      <div>48155 Ahlen</div>
      <div>E-Mail: info@karossa-vip.de</div>
      <div>Tel.: 0170-5558214</div>
      <div class="small">(24 Stunden erreichbar)</div>
      <div>www.karossa-fahrten.com</div>
      <div>www.karossa-vip.de</div>
    </div>
    <div class="card-brand">KAROSSA VIP</div>
  </section>

  <section class="business-card card-front">
    <div class="card-photo" role="img" aria-label="Foto einer weißen Stretchlimousine mit Fahrer vor einem Gebäude"></div>
    <svg width="320" height="186" viewBox="0 0 320 186" aria-hidden="true">
      <path d="M320,80 V186 H240 Q270,176 274,130 Q278,92 320,80 Z" fill="#1c1c1c"/>
    </svg>
    <div class="card-brand">KAROSSA VIP</div>
  </section>

  <div class="bottom-band"></div>
</main>
</body>
</html>
```